3 pages of UI design for AdTech Startup

We need 3 pages of UI design for a new AdTech company located in Seattle called KELVRA Systems.

We put digital, mobile billboards on college campuses throughout the country. This design project involves our back-end customer dashboard.

Page 1- Dashboard home page
page 2- Manage ads screen (see File 3 below for the screenshot of our current design). Please match the design of all 3 screens so there is consistency
page 3-Detailed Zone screen (see file 16 below). This page looks similar to the first page but gives a more detailed overview and a larger map.

The features and functionality are already built but we are lacking an aesthetically pleasing and slick design. Looking for someone who can match our website look to this new dashboard space. Our company reflects modern, clean, elegant design that is straight-forward and user friendly (main inspiration is TROVI, we love their design and feel).

Target Market(s)

-Local business owner, marketing directors, and national advertising and marketing agencies

Industry/Entity Type

Advertising

Number of Pages Required

3 page

Font styles to use
Other font styles liked:
• Proxima Nova- Thin for body text, Light for title

Colors
85cae6
33a6d7
0292cd
ffffff

Requirements
Nice to have
• Please include enough detail so that my developer can look at the design you come up with and translate it to html. Please include spacing, fonts, color numbers. My developer is going to look at your creation and recreate it in html format

```html
<!DOCTYPE html>
<html lang="en">
<head>
<meta charset="utf-8">
<title>Insights Summary – KELVRA Systems</title>
<link href="https://fonts.googleapis.com/css2?family=Lato:wght@300;400;700&display=swap" rel="stylesheet">
<style>
:root{
  --blue:#33a6d7;
  --blue-deep:#0292cd;
  --blue-soft:#85cae6;
  --footer:#35aee2;
  --ink:#333;
  --muted:#666;
  --line:#e4e4e4;
  --panel:#f6f6f6;
  --white:#fff;
  --dark:#555;
}
*{box-sizing:border-box;margin:0;padding:0}
html,body{width:1200px;height:894px;overflow:hidden;background:var(--white);font-family:'Lato',sans-serif;color:var(--ink)}
.page{position:relative;width:1200px;height:894px;border-top:3px solid var(--blue)}
.abs{position:absolute}
.header{left:0;top:0;width:1200px;height:63px;background:var(--panel);border-bottom:3px solid #e9e9e9}
.header .cell{position:absolute;top:0;height:63px;display:flex;align-items:center;border-right:1px solid var(--line);font-size:12px;color:var(--ink)}
.brand{left:0;width:104px;justify-content:center;font-weight:700;font-size:15px;color:var(--blue);letter-spacing:1px}
.crumb{left:104px;width:452px;padding-left:18px}
.client{left:556px;width:364px;padding-left:16px;border-left:1px solid var(--line)}
.client .league{font-weight:700;color:var(--blue-deep);margin-right:8px;font-size:12px}
.user{margin-left:auto;margin-right:20px;display:flex;align-items:center;gap:8px}
.avatar{width:28px;height:28px;border-radius:50%;background:#dcdcdc;border:2px solid #fff;box-shadow:0 0 0 1px #ccc}
.help{left:920px;width:280px;padding-left:24px;border-right:none}
.help .caret{position:absolute;right:26px;top:29px;border:5px solid transparent;border-top-color:#888}
.dates{left:17px;top:85px;font-size:12px;color:var(--ink)}
.toggle{left:667px;top:76px;display:flex;border:1px solid var(--line);background:var(--panel)}
.toggle span{display:block;height:30px;line-height:30px;font-size:12px;color:var(--ink);padding:0 15px;border-right:1px solid var(--line)}
.toggle span:last-child{border-right:none;padding:0 16px}
.toggle .on{background:var(--blue);color:#fff;padding:0 15px}
.chart{left:16px;top:117px;width:892px;height:348px;background:#fafafa;border:1px solid #ececec}
.chart text{font-family:'Lato',sans-serif;font-size:10px;fill:#555}
.stats{left:920px;top:66px;width:280px;height:399px;background:var(--panel)}
.stat{display:flex;height:51px;align-items:center;border-bottom:1px solid var(--line);font-size:12px}
.stat .k{width:102px;padding-left:23px;color:var(--muted)}
.stat .c{width:50px;color:var(--ink)}
.stat .v{font-weight:700;color:var(--ink)}
.tabs{left:16px;top:465px;width:1184px;height:49px;border-top:1px solid var(--line);border-bottom:1px solid var(--line)}
.tab{position:absolute;top:0;height:48px;display:flex;align-items:center;font-size:15px;color:var(--ink)}
.zone-perf{left:920px;top:465px;width:280px;height:49px;background:var(--white);padding-left:18px;display:flex;align-items:center;font-size:17px}
.zone-card{left:16px;top:522px;width:121px;height:269px;border:1px solid var(--line);text-align:center}
.zone-tag{position:absolute;left:12px;top:106px;width:96px;height:28px;background:var(--dark);color:#fff;font-size:13px;line-height:28px}
.zone-place{position:absolute;left:0;top:142px;width:100%;font-size:10px;color:var(--ink)}
.photo{left:150px;top:522px;width:170px;height:269px;background:linear-gradient(180deg,#b9b5a8 0%,#4a5058 45%,#2e3440 75%,#6c6a66 100%)}
.msg-btn{left:181px;top:731px;width:108px;height:32px;background:var(--blue);color:#fff;font-size:12px;text-align:center;line-height:32px}
.map{left:333px;top:522px;width:576px;height:269px;background:linear-gradient(135deg,#3f4a38 0%,#22303a 40%,#4a5442 70%,#2b3830 100%)}
.perf{left:920px;top:514px;width:280px;height:281px;background:var(--panel)}
.perf .stat{height:50px;font-size:14px}
.perf .stat .k{width:123px;padding-left:20px}
.perf .stat .c{width:16px}
.perf .stat .v{font-weight:400}
.btn-dark{left:940px;top:689px;width:96px;height:28px;background:var(--dark);color:#fff;font-size:11px;text-align:center;line-height:28px}
.btn-blue{left:1007px;top:742px;width:109px;height:32px;background:var(--blue);color:#fff;font-size:12px;text-align:center;line-height:32px}
.footer{left:0;top:830px;width:1200px;height:64px;background:var(--footer);color:#fff;font-size:11px;display:flex;align-items:center;padding:0 24px;justify-content:space-between}
.footer .mark{font-weight:700;font-size:15px;letter-spacing:1px}
</style>
</head>
<body>
<div class="page">
  <header class="header abs">
    <div class="cell brand">KELVRA</div>
    <div class="cell crumb">Insights Summary</div>
    <div class="cell client"><span class="league">LEAGUEONE</span>Marcus Hale
      <div class="user"><span class="avatar"></span>Evan Roper ▾</div>
    </div>
    <div class="cell help">Help ●<span class="caret"></span></div>
  </header>

  <div class="dates abs">2016-07-29 &nbsp;/&nbsp; 2016-08-05 &nbsp;▦</div>
  <div class="toggle abs"><span>Hourly</span><span class="on">Day</span><span>Week</span><span>Month</span></div>

  <div class="chart abs">
    <svg width="892" height="348" viewBox="0 0 892 348">
      <g stroke="#e6e6e6" stroke-width="1">
        <line x1="69" y1="30" x2="829" y2="30"/><line x1="69" y1="94.5" x2="829" y2="94.5"/>
        <line x1="69" y1="159" x2="829" y2="159"/><line x1="69" y1="223.5" x2="829" y2="223.5"/>
        <line x1="69" y1="288" x2="829" y2="288" stroke="#bcdcea"/>
      </g>
      <g text-anchor="end">
        <text x="42" y="33">100</text><text x="42" y="98">75</text><text x="42" y="162">50</text><text x="42" y="227">25</text><text x="42" y="291">0</text>
      </g>
      <circle cx="828" cy="29" r="3" fill="#333"/><text x="836" y="33" style="font-size:11px">Ads</text>
      <polygon fill="#eef7fc" points="62,288 139,260 217,257 294,252 367,239 446,30 527,236 602,249 678,257 756,265 836,288"/>
      <polygon fill="#f0f0f0" points="62,288 139,267 217,265 294,260 367,257 446,128 527,257 602,252 678,262 756,270 836,288"/>
      <polygon fill="#fff" points="62,288 139,276 217,275 294,272 367,270 446,221 527,270 602,269 678,274 756,278 836,288"/>
      <polyline fill="none" stroke="#a8d6ec" stroke-width="1.3" points="62,288 139,260 217,257 294,252 367,239 446,30 527,236 602,249 678,257 756,265 836,288"/>
      <polyline fill="none" stroke="#d4d4d4" stroke-width="1.3" points="62,288 139,267 217,265 294,260 367,257 446,128 527,257 602,252 678,262 756,270 836,288"/>
      <polyline fill="none" stroke="#33a6d7" stroke-width="1.5" points="62,288 139,276 217,275 294,272 367,270 446,221 527,270 602,269 678,274 756,278 836,288"/>
      <g fill="#33a6d7">
        <circle cx="139" cy="260" r="2.5"/><circle cx="217" cy="257" r="2.5"/><circle cx="294" cy="252" r="2.5"/><circle cx="367" cy="239" r="2.5"/><circle cx="446" cy="30" r="2.5"/><circle cx="527" cy="236" r="2.5"/><circle cx="602" cy="249" r="2.5"/><circle cx="678" cy="257" r="2.5"/><circle cx="756" cy="265" r="2.5"/>
        <circle cx="139" cy="276" r="2.5"/><circle cx="217" cy="275" r="2.5"/><circle cx="294" cy="272" r="2.5"/><circle cx="367" cy="270" r="2.5"/><circle cx="446" cy="221" r="2.5"/><circle cx="527" cy="270" r="2.5"/><circle cx="602" cy="269" r="2.5"/><circle cx="678" cy="274" r="2.5"/><circle cx="756" cy="278" r="2.5"/>
        <circle cx="62" cy="288" r="4"/><circle cx="836" cy="287" r="6"/>
      </g>
      <g fill="#ccc">
        <circle cx="139" cy="267" r="2.5"/><circle cx="217" cy="265" r="2.5"/><circle cx="294" cy="260" r="2.5"/><circle cx="367" cy="257" r="2.5"/><circle cx="446" cy="128" r="2.5"/><circle cx="527" cy="257" r="2.5"/><circle cx="602" cy="252" r="2.5"/><circle cx="678" cy="262" r="2.5"/><circle cx="756" cy="270" r="2.5"/>
      </g>
      <g text-anchor="middle">
        <text x="63" y="306">Jul 29,</text><text x="63" y="320">2016</text>
        <text x="137" y="306">Jul 30,</text><text x="137" y="320">2016</text>
        <text x="217" y="306">Jul 31,</text><text x="217" y="320">2016</text>
        <text x="294" y="306">Aug 01,</text><text x="294" y="320">2016</text>
        <text x="365" y="306">Aug 02,</text><text x="365" y="320">2016</text>
        <text x="440" y="306">Aug 03,</text><text x="440" y="320">2016</text>
        <text x="527" y="306">Aug 04,</text><text x="527" y="320">2016</text>
        <text x="601" y="306">Aug 05,</text><text x="601" y="320">2016</text>
        <text x="678" y="306">Aug 06,</text><text x="678" y="320">2016</text>
        <text x="757" y="306">Aug 07,</text><text x="757" y="320">2016</text>
        <text x="836" y="306">Aug 08,</text><text x="836" y="320">2016</text>
      </g>
    </svg>
  </div>

  <div class="stats abs">
    <div class="stat"><span class="k">Rotatins</span><span class="c">:</span><span class="v">85</span></div>
    <div class="stat"><span class="k">TIme</span><span class="c">:</span><span class="v">21:25 Min</span></div>
    <div class="stat"><span class="k">Impressions</span><span class="c">:</span><span class="v">595</span></div>
    <div class="stat"><span class="k">Miles</span><span class="c">:</span><span class="v">0.3 Miles</span></div>
  </div>

  <div class="tabs abs">
    <div class="tab" style="left:18px;width:120px;border-right:1px solid var(--line);height:30px;top:9px">Zoone</div>
    <div class="tab" style="left:134px;width:193px;border-right:1px solid var(--line)">Active Ad</div>
    <div class="tab" style="left:327px;width:581px;border-right:1px solid var(--line);padding-left:15px">Career Paths</div>
  </div>
  <div class="zone-perf abs">Zone Performance</div>

  <div class="zone-card abs"><div class="zone-tag">Zoone 1</div><div class="zone-place">Derek's House</div></div>
  <div class="photo abs" role="img" aria-label="Photo of two students walking on campus wearing backpacks with mounted digital ad screens"></div>
  <div class="msg-btn abs">Messages</div>
  <div class="map abs" role="img" aria-label="Satellite map of the Seattle area with outlined campus career path zones"></div>

  <div class="perf abs">
    <div class="stat"><span class="k">Rotatins</span><span class="c">:</span><span class="v">85</span></div>
    <div class="stat"><span class="k">Broadcast Time</span><span class="c">:</span><span class="v">21:25 Min</span></div>
    <div class="stat"><span class="k">Miles Walked</span><span class="c">:</span><span class="v">595</span></div>
  </div>
  <div class="btn-dark abs">Text Messages</div>
  <div class="btn-blue abs">Details</div>

  <footer class="footer abs"><span>2016 © Kelvra Campus.</span><span class="mark">KELVRA</span></footer>
</div>
</body>
</html>
```